Dine Slot Brochure

In need of a try-fold brochure.

This is for a new App that will help revolutionize the restaurant industry.

We need something that is creative but modern.
Look at the website in development for Ideas
http://brantoxstage.example/dineslotdev/restaurant/

This is an App for both the restaurant and the consumer -- but this brochure needs to be tailored towards the restaurant. All the content is already on the site but mix and play around with it.

Needs to have the Dine Slot Vs. Competitor Table -- maybe not all of it but some of it like the price points and software bit.

I will try to get a better logo file and update the brief as soon as I get it.
Updates

I will be in contact with the client over the weekend.  I will let you know changes by next week.

add the slogan: "No more waiting"

Target Market(s)

Restaurant owners
Restaurants that are busy with reservation all the time

Requirements
Must have
• QR code on the back
• link to website www.dineslotapp.example
• Social Media Tags
• Facebook, Twitter, Google+
• Icon for the following:
• Look at old brochure**
• "Get it on Vendra Shelf"
• "Available on the Pocket Bazaar"
Should not have
• I have attached their old brochure so you know exactly what NOT to do.

```html
<!DOCTYPE html>
<html lang="en">
<head>
<meta charset="utf-8">
<title>Dine Slot Brochure – Inside Spread</title>
<link rel="stylesheet" href="https://fonts.googleapis.com/css2?family=Oswald:wght@600;700&family=Cabin:wght@400&family=Nunito:wght@800&display=swap">
<style>
  :root {
    --cream: #f3ece2;
    --maroon: #a3314a;
    --maroon-soft: #c98393;
    --maroon-pale: #e7c9cf;
    --text-grey: #5e5a57;
    --bullet-grey: #8a8886;
    --white: #ffffff;
  }
  * { margin: 0; padding: 0; box-sizing: border-box; }
  html, body { width: 1200px; height: 844px; overflow: hidden; background: var(--cream); }
  .spread { position: relative; width: 1200px; height: 844px; background: var(--cream); overflow: hidden; }

  .hero-photo {
    position: absolute; left: 0; top: 0; width: 1200px; height: 170px;
    background: linear-gradient(90deg, #5a4232 0%, #a88868 22%, #7a5a44 45%, #c9b39a 62%, #8d6f58 80%, #b89e86 100%);
  }

  .tab {
    position: absolute; top: 161px; height: 43px; background: var(--maroon);
    color: var(--white); font-family: "Oswald", sans-serif; font-weight: 600;
    font-size: 25px; line-height: 43px; letter-spacing: -0.2px; white-space: nowrap;
    box-shadow: 0 3px 5px rgba(0,0,0,.3);
  }
  .tab--restaurant { left: 0; width: 302px; border-radius: 0 22px 22px 0; padding-left: 30px; }
  .tab--customer { left: 433px; width: 332px; border-radius: 22px; text-align: center; }
  .tab--features { left: 950px; width: 250px; border-radius: 22px 0 0 22px; text-align: right; padding-right: 29px; }

  .restaurant-list { position: absolute; left: 0; top: 0; list-style: none; }
  .restaurant-list li {
    position: absolute; left: 64px; font-family: "Cabin", sans-serif;
    font-size: 18px; line-height: 18px; letter-spacing: 0.2px; color: var(--text-grey); white-space: nowrap;
  }
  .restaurant-list li::before {
    content: ""; position: absolute; left: -33px; top: 2px; width: 11px; height: 11px;
    border-radius: 50%; background: var(--maroon);
  }
  .restaurant-list .indent { padding-left: 22px; display: block; }

  .customer-list {
    position: absolute; left: 408px; top: 223px; width: 380px; text-align: center;
    font-family: "Cabin", sans-serif; font-size: 18px; line-height: 19px; letter-spacing: 0.2px; color: var(--text-grey);
  }
  .customer-list p { margin-bottom: 16px; white-space: nowrap; }

  .slogan-lettering {
    position: absolute; left: 503px; top: 546px; width: 190px; height: 66px;
    background: var(--maroon-pale); border-radius: 8px;
  }

  .feature-list { position: absolute; left: 0; top: 0; list-style: none; }
  .feature-list li {
    position: absolute; left: 851px; font-family: "Nunito", sans-serif; font-weight: 800;
    font-size: 21px; line-height: 22px; color: var(--maroon); white-space: nowrap;
  }
  .feature-list li::before {
    content: ""; position: absolute; left: -26px; top: 5px; width: 12px; height: 12px;
    border-radius: 50%; background: var(--bullet-grey);
  }

  .benefits-heading {
    position: absolute; left: 490px; top: 618px; font-family: "Oswald", sans-serif; font-weight: 700;
    font-size: 31px; line-height: 36px; letter-spacing: -0.5px; color: var(--maroon); z-index: 2;
  }
  .benefits-panel {
    position: absolute; left: 418px; top: 652px; width: 782px; height: 192px;
    background: var(--maroon); border-radius: 48px 0 0 0;
  }
  .benefit-list { position: absolute; left: 0; top: 0; list-style: none; }
  .benefit-list li {
    position: absolute; font-family: "Nunito", sans-serif; font-weight: 800; font-size: 18.5px;
    line-height: 18px; color: var(--white); white-space: nowrap;
  }
  .benefit-list li::before {
    content: ""; position: absolute; left: -49px; top: 3px; width: 12px; height: 12px;
    border-radius: 50%; background: var(--white);
  }

  .table-setting-photo {
    position: absolute; left: 122px; top: 714px; width: 154px; height: 130px;
    background: linear-gradient(135deg, #ddd2c4 0%, #c9bcac 100%);
  }
  .table-setting-photo::after {
    content: ""; position: absolute; left: 22px; top: 26px; width: 110px; height: 78px;
    background: #b8293a; border-radius: 6px;
  }
</style>
</head>
<body>
<main class="spread">
  <div class="hero-photo" role="img" aria-label="Photo of a smiling couple toasting with wine glasses in a busy restaurant"></div>

  <h2 class="tab tab--restaurant">Restaurant’s Perspective...</h2>
  <h2 class="tab tab--customer">Customer’s Perspective...</h2>
  <h2 class="tab tab--features">Features</h2>

  <ul class="restaurant-list">
    <li style="top:228px">True Real Time Table Reservation</li>
    <li style="top:271px">GPS Enabled Search Function</li>
    <li style="top:313px">Post Special Offers Instantly</li>
    <li style="top:356px">Real Time SMS confirmation, Alerts<span class="indent">and Loyalty Reward Notification!</span></li>
    <li style="top:415px">“Opt-In” Email Capturing for<span class="indent">Email Marketing</span></li>
    <li style="top:476px">Manageable Customer Reviews</li>
    <li style="top:518px">Reduce Human Errors and Overhead<span class="indent">Cost Associated with Employees</span></li>
    <li style="top:579px">Built in Loyalty System to Track<span class="indent">and Reward Loyal Customers</span></li>
    <li style="top:638px">Full Support + IT Solutions available</li>
    <li style="top:680px">Designed by Actual Restaurant Owner</li>
  </ul>

  <div class="customer-list">
    <p>No More Waiting For A Table!</p>
    <p>GPS Enabled Search Allow You to Find<br>The Nearest Delicious Restaurant!</p>
    <p>Search For New Restaurants using<br>Real Time Special Offers!</p>
    <p>Receive Instant SMS messages for<br>Confirmation, Reminder and Loyalty Rewards</p>
    <p>Automatically Receive Rewards for being<br>Loyal To Your Favorite Restaurants!</p>
    <p>Guaranteed Table for Seating When You Arrive</p>
    <p>Simple Control and Ease of Use</p>
  </div>

  <div class="slogan-lettering" role="img" aria-label="Hand-lettered script slogan in maroon: The Wait is Over, with a swoosh underline"></div>

  <ul class="feature-list">
    <li style="top:216px">It's all about now!</li>
    <li style="top:259px">Confirming your reservation?</li>
    <li style="top:302px">Capture Customer Emails!</li>
    <li style="top:344px">Tables and Rewards!</li>
    <li style="top:387px">Managing your reviews!</li>
    <li style="top:430px">Real Time Offer Creation!</li>
    <li style="top:473px">Real Time Table Management!</li>
    <li style="top:515px">Manage your floor</li>
    <li style="top:558px">Built in Loyalty Rewards</li>
    <li style="top:601px">Managing Your Reviews</li>
  </ul>

  <h2 class="benefits-heading">Benefits</h2>
  <section class="benefits-panel"></section>
  <ul class="benefit-list">
    <li style="left:514px;top:671px">Social Media Promotion</li>
    <li style="left:514px;top:698px">GPS Based Search</li>
    <li style="left:514px;top:725px">Real Time Advertisements</li>
    <li style="left:514px;top:752px">Freedom to access anytime and anywhere</li>
    <li style="left:514px;top:779px">Fast and Easy setup with no training required</li>
    <li style="left:817px;top:671px">Manage your table reservations</li>
    <li style="left:817px;top:698px">Managing Your Reviews</li>
    <li style="left:817px;top:725px">Email Marketing</li>
    <li style="left:998px;top:752px">Cost &amp; Value</li>
  </ul>

  <div class="table-setting-photo" role="img" aria-label="Photo of a table setting with a red folded napkin and silver fork on a red plate"></div>
</main>
</body>
</html>
```